Northern Terrain Published Photographer Website

I need a website to feature a home page slide show of 6 of my top photos then a few simple pages including; gallery, bio, social, checkout, services
Updates

Need extra days to review

Target Market(s)

photography

Industry/Entity Type

Photographer

Coding

Coded - Design and coding required

Number of Pages Required

5+ page

Colors

Designer to choose colors to be used in the design.

Requirements
Must have
• clean eye catching elegant trendy
Nice to have
• unique and creative from other photographer websites

```html
<!DOCTYPE html>
<html lang="en">
<head>
<meta charset="utf-8">
<title>Northern Terrain — Marla Thorne Photography</title>
<link href="https://fonts.googleapis.com/css2?family=Nunito:wght@800;900&family=Mulish:wght@400;600;700&display=swap" rel="stylesheet">
<style>
:root{
  --black:#000;
  --panel:#0d0d0d;
  --footer:#0b0b0b;
  --orange:#f5a000;
  --white:#fff;
  --muted:#8a8a8a;
  --soft:#bdbdbd;
}
*{margin:0;padding:0;box-sizing:border-box}
html,body{width:1200px;height:4465px;overflow:hidden;background:var(--black)}
body{position:relative;font-family:"Mulish",sans-serif;color:var(--white)}
.abs{position:absolute}
.photo{position:absolute;display:block}
.heading{font-family:"Nunito",sans-serif;font-weight:900;color:var(--white)}
.rule{position:absolute;height:3px;background:var(--orange)}
.btn{position:absolute;border:1px solid var(--orange);border-right:none;color:var(--orange);font-size:15px;display:flex;align-items:center;justify-content:center}
.muted{color:var(--muted);font-size:12.5px;line-height:19px}
.more{color:var(--orange)}

/* hero */
.hero{position:absolute;left:0;top:0;width:1200px;height:635px;background:#1a1512}
.hero-panel{position:absolute;left:0;top:0;width:303px;height:635px;background:var(--black)}
.logo{position:absolute;font-size:22px;font-weight:400;color:var(--white);letter-spacing:.5px;display:flex;align-items:center;gap:8px}
.logo i{width:9px;height:9px;border-radius:50%;background:var(--white);display:inline-block}
.nav{position:absolute;top:25px;left:626px;display:flex;font-size:11.5px}
.nav a{color:var(--white);text-decoration:none;padding:7px 10px;margin-right:3px}
.nav a.active{border:1px solid var(--orange)}
.hero h1{position:absolute;left:93px;top:170px;font-size:48px;line-height:62px}
.hero p{position:absolute;left:93px;top:378px;width:620px;font-size:16.5px;line-height:20px;color:#eee}
.side-links{position:absolute;left:1116px;top:172px;font-size:13px;color:var(--white)}
.side-links span{position:absolute;writing-mode:vertical-rl;white-space:nowrap;display:flex;align-items:center;gap:6px}
.side-links span::before{content:"";width:9px;height:9px;background:var(--white);display:inline-block}
.counter{position:absolute;left:1090px;top:580px;font-size:13px;color:var(--white)}
.counter b{color:var(--orange);font-weight:400;font-size:16px}

/* about */
.about{position:absolute;left:0;top:635px;width:1200px;height:615px;background:var(--panel)}

/* categories */
.categories{position:absolute;left:0;top:1250px;width:1200px;height:938px;background:var(--black)}
.title-center{position:absolute;left:0;width:1200px;text-align:center;font-size:34px}
.filters{position:absolute;top:196px;left:0;width:1200px;display:flex;justify-content:center;gap:22px;font-size:11.5px;color:var(--white);align-items:center}
.filters .dot{width:4px;height:4px;border-radius:50%;background:#aaa}
.filters .on{color:var(--orange);border-bottom:1px solid var(--orange)}

/* why */
.why{position:absolute;left:0;top:2188px;width:1200px;height:1602px;background:linear-gradient(#161616,#0e0e0e 50%,#121212)}
.feature{position:absolute;width:310px;text-align:center}
.feature .icon{width:66px;height:66px;border:1px solid var(--orange);margin:0 auto;display:flex;align-items:center;justify-content:center;border-radius:3px}
.feature h3{font-family:"Nunito",sans-serif;font-weight:800;font-size:17px;margin-top:32px;letter-spacing:.3px}
.feature p{margin-top:10px;font-size:12px;line-height:19.5px;color:var(--muted)}

/* news */
.news-item h4{font-family:"Nunito",sans-serif;font-weight:800;font-size:14px;position:absolute;left:827px}

/* newsletter */
.newsletter{position:absolute;left:0;top:3790px;width:1200px;height:354px;background:radial-gradient(ellipse at 50% 35%,#5a3418 0%,#2a1a10 45%,#120c08 100%)}
.field{position:absolute;left:245px;top:214px;width:544px;height:59px;border:1px solid #777;background:#0b0b0b;font-size:12px;color:#9a9a9a;display:flex;align-items:center;padding-left:20px}
.sub-btn{position:absolute;left:789px;top:214px;width:165px;height:59px;background:var(--orange);color:#111;font-family:"Nunito",sans-serif;font-weight:900;font-size:20px;display:flex;align-items:center;justify-content:center}

/* footer */
.footer{position:absolute;left:0;top:4144px;width:1200px;height:321px;background:var(--footer)}
.footer h5{position:absolute;font-family:"Nunito",sans-serif;font-weight:800;font-size:16px;top:82px}
.thumb{position:absolute;width:61px;height:43px}
</style>
</head>
<body>

<section class="hero">
  <div class="hero-panel"></div>
  <div class="photo" role="img" aria-label="Horseshoe-shaped canyon with a green river bend at dusk" style="left:303px;top:0;width:897px;height:635px;background:linear-gradient(170deg,#5b4338 0%,#8b4a2a 35%,#4a2f22 55%,#26463e 70%,#1b1714 100%)"></div>
  <div class="logo" style="left:95px;top:22px">Marla Thorne<i></i></div>
  <nav class="nav">
    <a class="active">HOME</a><a>GALLERY</a><a>BIO</a><a>SOCIAL</a><a>CHECKOUT</a><a>SERVICES</a><a>CONTACTS</a>
  </nav>
  <h1 class="heading">My Name Is Marla Thorne<br>I’m a Photographer</h1>
  <div class="rule" style="left:93px;top:321px;width:83px"></div>
  <p>Cras ultrices nunc eu turpis venenatis, sed gravida ante consectetur. Morbi bibendum mauris eros, vel interdum arcu tempus sed.</p>
  <div class="btn" style="left:94px;top:474px;width:89px;height:32px">View More</div>
  <div class="side-links">
    <span style="top:0">Journal</span>
    <span style="top:128px">Notes</span>
    <span style="top:238px">Stories</span>
  </div>
  <div class="counter"><b>01</b> / 06</div>
</section>

<section class="about">
  <div class="photo" role="img" aria-label="Arched bridge over a misty waterfall in an autumn gorge" style="left:94px;top:86px;width:444px;height:451px;background:linear-gradient(160deg,#d9dde0 0%,#9aa69a 30%,#6e6b3a 55%,#8d6a2c 75%,#3e3a2a 100%)"></div>
  <h2 class="heading abs" style="left:598px;top:124px;font-size:33px;line-height:47px">My Name Is Marla Thorne<br>I’m a Photographer</h2>
  <div class="rule" style="left:599px;top:247px;width:83px"></div>
  <p class="muted abs" style="left:599px;top:302px;width:470px">Cras ultrices nunc eu turpis venenatis, sed gravida ante consectetur. Morbi bibendum mauris eros, vel interdum arcu tempus sed. Duis quis aliquam lorem. Nullam volutpat consequat nisi eu congue. Aenean vitae tellus posuere, pretium nisl vitae, congue nisi. Proin odio ipsum, pulvinar id nisi sit amet, malesuada consequat dui. Vestibulum vel nisi sit amet nunc sollicitudin feugiat.</p>
  <div class="btn" style="left:600px;top:456px;width:89px;height:32px">Read More</div>
</section>

<section class="categories">
  <h2 class="heading title-center" style="top:82px">CATEGORIES</h2>
  <div class="rule" style="left:560px;top:138px;width:80px"></div>
  <div class="filters">
    <span class="on">ALL</span><i class="dot"></i><span>FOREST</span><i class="dot"></i><span>HILL</span><i class="dot"></i><span>MOUNTAIN</span><i class="dot"></i><span>PORTRAITS</span><i class="dot"></i><span>ANIMALS</span><i class="dot"></i><span>ABSTRUCT</span>
  </div>
  <div class="photo" role="img" aria-label="Canyon rim under purple storm clouds" style="left:94px;top:293px;width:298px;height:219px;background:linear-gradient(#3b3550,#7a4c46 45%,#b5552c 70%,#4a2a20)"></div>
  <div class="photo" role="img" aria-label="Snowy forested cliffs reflected in a still lake" style="left:428px;top:293px;width:344px;height:479px;background:linear-gradient(#6f9fd6,#cfdff0 30%,#4a5a44 52%,#d8dce0 62%,#7fa2c8 80%,#2a3a30)"></div>
  <div class="photo" role="img" aria-label="Golden sunset over a pier with a silhouetted bird" style="left:808px;top:293px;width:298px;height:219px;background:linear-gradient(#4a3410,#d98a10 45%,#f5b020 55%,#6a4510)"></div>
  <div class="photo" role="img" aria-label="Layered canyon ridges under a cloudy sky" style="left:94px;top:552px;width:298px;height:220px;background:linear-gradient(#7a8ca8,#b9c1cc 35%,#8a7b6a 60%,#4e4338)"></div>
  <div class="photo" role="img" aria-label="Glass sphere on a beach at a violet sunset" style="left:808px;top:552px;width:298px;height:220px;background:linear-gradient(#3d2f8a,#8a66c8 45%,#c99ad8 60%,#4b3a7a)"></div>
  <div class="btn" style="left:551px;top:838px;width:88px;height:32px">View More</div>
</section>

<section class="why">
  <h2 class="heading title-center" style="top:92px">WHY CHOOSE ME?</h2>
  <div class="rule" style="left:560px;top:149px;width:80px"></div>

  <div class="feature" style="left:90px;top:243px">
    <div class="icon"><svg width="26" height="26" viewBox="0 0 26 26" fill="none" stroke="#f5a000" stroke-width="2"><rect x="6" y="5" width="14" height="10"/><circle cx="13" cy="10" r="3"/><path d="M13 15v8M8 23h10"/></svg></div>
    <h3>LIGHT COMPOSURE</h3>
    <p>Cras ultrices nunc eu turpis venenatis, sed gravida ante consectetur. Morbi bibendum mauris eros, vel interdum arcu tempus sed. <span class="more">[...]</span></p>
  </div>
  <div class="feature" style="left:445px;top:243px">
    <div class="icon"><svg width="26" height="26" viewBox="0 0 26 26" fill="none" stroke="#f5a000" stroke-width="2"><circle cx="13" cy="8" r="4"/><path d="M5 23c0-5 4-8 8-8s8 3 8 8z"/></svg></div>
    <h3>PROFESSIONAL SKILLS</h3>
    <p>Cras ultrices nunc eu turpis venenatis, sed gravida ante consectetur. Morbi bibendum mauris eros, vel interdum arcu tempus sed. <span class="more">[...]</span></p>
  </div>
  <div class="feature" style="left:799px;top:243px">
    <div class="icon"><svg width="26" height="26" viewBox="0 0 26 26"><path d="M3 8h5l2-3h6l2 3h5v14H3z" fill="#f5a000"/><circle cx="13" cy="14" r="4" fill="#121212"/></svg></div>
    <h3>PERFECT EQUIPMENT</h3>
    <p>Cras ultrices nunc eu turpis venenatis, sed gravida ante consectetur. Morbi bibendum mauris eros, vel interdum arcu tempus sed. <span class="more">[...]</span></p>
  </div>
  <div class="feature" style="left:90px;top:468px">
    <div class="icon"><svg width="26" height="26" viewBox="0 0 26 26" fill="none" stroke="#f5a000" stroke-width="2"><rect x="6" y="4" width="16" height="12"/><rect x="3" y="13" width="8" height="8"/></svg></div>
    <h3>ULTRA HD</h3>
    <p>Cras ultrices nunc eu turpis venenatis, sed gravida ante consectetur. Morbi bibendum mauris eros, vel interdum arcu tempus sed. <span class="more">[...]</span></p>
  </div>
  <div class="feature" style="left:445px;top:468px">
    <div class="icon"><svg width="26" height="26" viewBox="0 0 26 26" fill="none" stroke="#f5a000" stroke-width="2"><path d="M3 8V3h5M18 3h5v5M23 18v5h-5M8 23H3v-5"/><ellipse cx="13" cy="13" rx="6" ry="3.5"/><circle cx="13" cy="13" r="1.5" fill="#f5a000"/></svg></div>
    <h3>UNIC VISION</h3>
    <p>Cras ultrices nunc eu turpis venenatis, sed gravida ante consectetur. Morbi bibendum mauris eros, vel interdum arcu tempus sed. <span class="more">[...]</span></p>
  </div>
  <div class="feature" style="left:799px;top:468px">
    <div class="icon"><svg width="26" height="26" viewBox="0 0 26 26" fill="none" stroke="#f5a000" stroke-width="2"><circle cx="13" cy="13" r="9"/><circle cx="13" cy="13" r="4"/><path d="M13 4l2 5M22 13l-5 2M13 22l-2-5M4 13l5-2"/></svg></div>
    <h3>FOCUSING KNOWLEDGES</h3>
    <p>Cras ultrices nunc eu turpis venenatis, sed gravida ante consectetur. Morbi bibendum mauris eros, vel interdum arcu tempus sed. <span class="more">[...]</span></p>
  </div>

  <h2 class="heading title-center" style="top:836px">LATEST NEWS</h2>
  <div class="rule" style="left:560px;top:893px;width:80px"></div>

  <div class="photo" role="img" aria-label="Fiery red sunset sky over snowy pine forest" style="left:94px;top:982px;width:466px;height:300px;background:linear-gradient(#5a1e1a,#d84a20 35%,#f08a30 55%,#3a2a2a 75%,#d8d8e0)"></div>
  <div class="abs" style="left:450px;top:1260px;font-size:14px;font-weight:700;color:var(--orange)">13 Freb,2019</div>
  <h3 class="abs" style="left:94px;top:1326px;font-family:'Nunito',sans-serif;font-weight:800;font-size:17px;line-height:25px">Pellentesque laoreet pretium dictum.<br>Phasellus et convallis mauris.</h3>
  <div class="rule" style="left:94px;top:1400px;width:83px"></div>
  <p class="muted abs" style="left:94px;top:1437px;width:440px;font-size:12px">Cras ultrices nunc eu turpis venenatis, sed gravida ante consectetur. Morbi bibendum mauris eros, vel interdum arcu tempus sed. Duis quis aliquam lorem. Nullam volutpat consequat nisi eu congue. <span class="more">[...]</span></p>

  <div class="news-item">
    <div class="photo" role="img" aria-label="Sandstone butte reflected in calm water" style="left:600px;top:978px;width:192px;height:137px;background:linear-gradient(#5a8ab8,#c8883a 50%,#3a4a58)"></div>
    <h4 style="top:994px">Pellentesque laoreet pretium dictum.</h4>
    <div class="rule" style="left:827px;top:1028px;width:83px"></div>
    <p class="muted abs" style="left:827px;top:1060px;width:280px;font-size:12px">Cras ultrices nunc eu turpis venenatis, sed gravida ante consectetur. Morbi bibendum mauris eros. <span class="more">[...]</span></p>
  </div>
  <div class="news-item">
    <div class="photo" role="img" aria-label="Bighorn sheep in a desert valley" style="left:600px;top:1167px;width:192px;height:137px;background:linear-gradient(#6a8ec0,#b09070 50%,#7a5a48)"></div>
    <h4 style="top:1182px">Pellentesque laoreet pretium dictum.</h4>
    <div class="rule" style="left:827px;top:1216px;width:83px"></div>
    <p class="muted abs" style="left:827px;top:1248px;width:280px;font-size:12px">Cras ultrices nunc eu turpis venenatis, sed gravida ante consectetur. Morbi bibendum mauris eros. <span class="more">[...]</span></p>
  </div>
  <div class="news-item">
    <div class="photo" role="img" aria-label="Snowcapped mountain range above red desert at dusk" style="left:600px;top:1355px;width:192px;height:137px;background:linear-gradient(#2a3a68,#8a9ac0 45%,#5a3a40 70%,#2a1e22)"></div>
    <h4 style="top:1370px">Pellentesque laoreet pretium dictum.</h4>
    <div class="rule" style="left:827px;top:1404px;width:83px"></div>
    <p class="muted abs" style="left:827px;top:1436px;width:280px;font-size:12px">Cras ultrices nunc eu turpis venenatis, sed gravida ante consectetur. Morbi bibendum mauris eros. <span class="more">[...]</span></p>
  </div>
</section>

<section class="newsletter" role="img" aria-label="Desert mesa landscape at dusk behind the newsletter signup">
  <h2 class="heading title-center" style="top:78px">SUBSCRIBE MY NEWSLETTER</h2>
  <p class="abs" style="left:0;width:1200px;top:162px;text-align:center;font-size:12px;color:var(--soft)">Subscribe and get my latest photos and news.</p>
  <div class="field">Enter your email address...</div>
  <div class="sub-btn">Subscribe</div>
</section>

<footer class="footer">
  <div class="logo" style="left:94px;top:72px">Marla Thorne<i></i></div>
  <p class="muted abs" style="left:94px;top:144px;width:260px;font-size:12px">Cras ultrices nunc eu turpis venenatis, sed gravida ante consectetur. Morbi bibendum mauris eros, vel interdum arcu tempus sed. Duis quis aliquam lorem.sit amet nunc sollicitudin feugiat.</p>

  <h5 style="left:451px">LATEST PHOTOS</h5>
  <div class="thumb" role="img" aria-label="Butte reflection" style="left:451px;top:144px;background:linear-gradient(#5a8ab8,#c8883a)"></div>
  <div class="thumb" role="img" aria-label="Dusk canyon" style="left:525px;top:144px;background:linear-gradient(#3a2a2a,#b0602a)"></div>
  <div class="thumb" role="img" aria-label="Red sunset" style="left:600px;top:144px;background:linear-gradient(#c83a20,#f08a30)"></div>
  <div class="thumb" role="img" aria-label="Mountain range" style="left:451px;top:203px;background:linear-gradient(#2a3a68,#8a9ac0)"></div>
  <div class="thumb" role="img" aria-label="Desert valley" style="left:525px;top:203px;background:linear-gradient(#6a8ec0,#b09070)"></div>
  <div class="thumb" role="img" aria-label="Golden pier" style="left:600px;top:203px;background:linear-gradient(#4a3410,#d98a10)"></div>

  <h5 style="left:784px">CONTACTS</h5>
  <p class="muted abs" style="left:784px;top:144px;font-size:12px">Phone: +1 (555) 014 2290<br>Email: hello@northernterrain.example</p>
  <p class="abs" style="left:784px;top:218px;font-size:12px;color:var(--orange)">Copyright © 2019 Logo Goes There. All Rights Reserved.</p>
</footer>

</body>
</html>
```